Business Card

I would like a business card with a picture of my husband and I that is unique and professional.

Industry/Entity Type

Business

Font styles to use
Serif

```html
<!DOCTYPE html>
<html lang="en">
<head>
<meta charset="utf-8">
<title>Whitmore Leadership Development – Business Card</title>
<link rel="stylesheet" href="https://fonts.googleapis.com/css2?family=Cinzel:wght@500;700&family=Open+Sans:wght@300;400&display=swap">
<style>
  :root {
    --stage: #d9d9d9;
    --card: #141414;
    --card-edge: #0a0a0a;
    --gold: #d9a93f;
    --gold-soft: #b98a2c;
    --text-light: #e6e6e6;
    --text-muted: #bdbdbd;
    --rule: #8a8a8a;
    --photo-top: #3a3a3a;
    --photo-bottom: #8c8c8c;
  }
  * { box-sizing: border-box; margin: 0; padding: 0; }
  html, body { width: 1200px; height: 900px; overflow: hidden; }
  body {
    background: radial-gradient(ellipse at 55% 45%, #f2f2f2 0%, var(--stage) 70%);
    position: relative;
    font-family: "Open Sans", sans-serif;
  }
  .card {
    position: absolute;
    width: 700px;
    height: 400px;
    background: linear-gradient(160deg, #1e1e1e 0%, var(--card) 60%, var(--card-edge) 100%);
    box-shadow: 0 14px 30px rgba(0,0,0,.35);
    overflow: hidden;
  }
  .card--front { left: 250px; top: 30px; }
  .card--back  { left: 250px; top: 470px; }

  /* Front */
  .brand-mark {
    position: absolute;
    left: 0; right: 0; top: 95px;
    display: flex; align-items: center; justify-content: center; gap: 16px;
  }
  .brand-mark__dot {
    width: 22px; height: 22px; border-radius: 50%;
    background: var(--gold);
  }
  .brand-mark__name {
    font-family: "Cinzel", serif;
    font-weight: 700;
    font-size: 58px;
    color: var(--gold);
    letter-spacing: 3px;
  }
  .company-line {
    position: absolute;
    left: 0; right: 0;
    display: flex; flex-direction: column; align-items: center;
  }
  .card--front .company-line { top: 270px; }
  .company-line__name {
    font-family: "Cinzel", serif;
    font-weight: 700;
    font-size: 26px;
    color: var(--gold);
    letter-spacing: 1px;
  }
  .company-line__rule { margin-top: 6px; }

  /* Back */
  .person {
    position: absolute; left: 40px; top: 40px; width: 380px;
  }
  .person__name {
    font-family: "Cinzel", serif;
    font-weight: 500;
    font-size: 28px;
    color: var(--gold);
    letter-spacing: 3px;
  }
  .person__title {
    font-size: 12px;
    color: var(--text-muted);
    letter-spacing: 1.5px;
    text-transform: uppercase;
    padding-bottom: 8px;
    border-bottom: 1px dotted var(--rule);
  }
  .contact {
    list-style: none;
    margin-top: 10px;
    padding-bottom: 10px;
    border-bottom: 1px dotted var(--rule);
  }
  .contact__item {
    display: flex; align-items: center; gap: 12px;
    font-size: 16px; font-weight: 300;
    color: var(--text-light);
    line-height: 27px;
  }
  .contact__item svg { flex: none; }
  .address {
    margin-top: 8px;
    font-size: 16px; font-weight: 300;
    color: var(--text-light);
  }
  .card--back .company-line {
    left: 30px; right: auto; top: 290px; width: 370px;
  }
  .card--back .company-line__name { font-size: 19px; }
  .couple-photo {
    position: absolute;
    right: 0; top: 60px;
    width: 300px; height: 340px;
    background: linear-gradient(180deg, var(--photo-top) 0%, var(--photo-bottom) 100%);
  }
</style>
</head>
<body>

  <section class="card card--front" aria-label="Card front">
    <div class="brand-mark">
      <span class="brand-mark__dot"></span>
      <span class="brand-mark__name">Whitmore</span>
    </div>
    <div class="company-line">
      <span class="company-line__name">WHITMORE LEADERSHIP DEVELOPMENT</span>
      <svg class="company-line__rule" width="500" height="6" viewBox="0 0 500 6" aria-hidden="true">
        <line x1="0" y1="3" x2="500" y2="3" stroke="var(--gold-soft)" stroke-width="1.5"/>
      </svg>
    </div>
  </section>

  <section class="card card--back" aria-label="Card back">
    <div class="person">
      <h1 class="person__name">DANA WHITMORE</h1>
      <p class="person__title">Professional Mentorship Strategist</p>
      <ul class="contact">
        <li class="contact__item">
          <svg width="16" height="16" viewBox="0 0 24 24" aria-hidden="true"><path d="M6.6 10.8a15 15 0 0 0 6.6 6.6l2.2-2.2a1 1 0 0 1 1-.25 11 11 0 0 0 3.6.6 1 1 0 0 1 1 1V20a1 1 0 0 1-1 1A17 17 0 0 1 3 4a1 1 0 0 1 1-1h3.5a1 1 0 0 1 1 1 11 11 0 0 0 .6 3.6 1 1 0 0 1-.25 1z" fill="var(--text-light)"/></svg>
          <span>: 555-014-2288 Direct</span>
        </li>
        <li class="contact__item">
          <svg width="16" height="16" viewBox="0 0 24 24" aria-hidden="true"><rect x="2" y="5" width="20" height="14" fill="none" stroke="var(--text-light)" stroke-width="1.6"/><path d="M2 5l10 8 10-8" fill="none" stroke="var(--text-light)" stroke-width="1.6"/></svg>
          <span>: dana@whitmoremail.com</span>
        </li>
        <li class="contact__item">
          <svg width="16" height="16" viewBox="0 0 24 24" aria-hidden="true"><circle cx="12" cy="12" r="10" fill="none" stroke="var(--text-light)" stroke-width="1.6"/><ellipse cx="12" cy="12" rx="4.5" ry="10" fill="none" stroke="var(--text-light)" stroke-width="1.4"/><line x1="2" y1="12" x2="22" y2="12" stroke="var(--text-light)" stroke-width="1.4"/></svg>
          <span>: www.yoursite.com</span>
        </li>
      </ul>
      <p class="address">Your address go here</p>
    </div>
    <div class="company-line">
      <span class="company-line__name">WHITMORE LEADERSHIP DEVELOPMENT</span>
      <svg class="company-line__rule" width="370" height="6" viewBox="0 0 370 6" aria-hidden="true">
        <line x1="0" y1="3" x2="370" y2="3" stroke="var(--gold-soft)" stroke-width="1.5"/>
      </svg>
    </div>
    <div class="couple-photo" role="img" aria-label="Portrait photo of the husband and wife"></div>
  </section>

</body>
</html>
```